Wine Label Design for Ferrant Estate

I need a front and back label for a new wine I am making. I am looking for a classic, elegant and serious wine label. I would like the label to be white with blue and black writing. The blue will be the distinction in the label. The color of blue will be unique and catch the eye. The font of the writing will be unique and could also serve as the brand image for Ferrant Estate. The label can have a design but should be simple and distinct. I envision the paper quality of the label to textured, high quality and add to the overall image of the label.
The label will be timeless. The price of this wine will be $85.00 a bottle, and the label should match a higher priced wine. This wine is family owned and operated.
The writing on the front and back label will be:

FRONT Label-

Ferrant Estate

Howell Mountain

Napa Valley

2022 Cabernet Sauvignon

Back Label-

Cellared and Bottled by Ferrant Estate, Angwin, CA 94508

GOVERNMENT WARNING: (1) According to the Surgeon General, women should not drink alcoholic beverages during pregnancy because of the risk of birth defects. (2) Consumption of alcoholic beverages impairs your ability to drive a car or operate machinery, and may cause health problems.

Alc. 14.5% by Vol.

750 ml

Contains Sulfites

```html
<!DOCTYPE html>
<html lang="en">
<head>
<meta charset="utf-8">
<title>Ferrant Estate – 2022 Cabernet Sauvignon Labels</title>
<link rel="stylesheet" href="https://fonts.googleapis.com/css2?family=Playfair+Display:wght@600;700&family=Archivo:wght@400;500;600&family=Libre+Caslon+Text:wght@400&display=swap">
<style>
  :root {
    --paper: #f2eee5;
    --paper-edge: #d9d2c3;
    --ink-navy: #1e2840;
    --ink-dark: #222630;
    --ink-body: #3a3d45;
    --copper: #a8703b;
    --copper-soft: #c99a62;
    --band: #1b2233;
    --band-line: #8a6a45;
    --rule: #8d8778;
    --page: #ffffff;
    --serif: "Playfair Display", Georgia, serif;
    --sans: "Archivo", Arial, sans-serif;
    --text: "Libre Caslon Text", Georgia, serif;
  }
  * { margin: 0; padding: 0; box-sizing: border-box; }
  html, body { width: 1200px; height: 1200px; overflow: hidden; background: var(--page); }
  .canvas { position: relative; width: 1200px; height: 1200px; }
  .abs { position: absolute; }
  .center { left: 0; right: 0; text-align: center; }

  /* Front label */
  .front-main {
    left: 6px; top: 18px; width: 592px; height: 826px;
    background: var(--paper);
    border: 1px solid var(--paper-edge);
    border-radius: 26px 26px 4px 4px;
    box-shadow: 0 2px 6px rgba(0,0,0,.12);
  }
  .front-main .frame {
    position: absolute; inset: 16px;
    border: 1px solid var(--copper-soft);
    border-radius: 18px 18px 2px 2px;
  }
  .brand-name {
    top: 142px; font-family: var(--serif); font-weight: 700;
    font-size: 84px; letter-spacing: 2px; color: var(--ink-navy); line-height: 1;
  }
  .brand-sub {
    top: 262px; font-family: var(--serif); font-weight: 600;
    font-size: 48px; letter-spacing: 3px; color: var(--ink-navy); line-height: 1;
  }
  .vineyard-art {
    left: 47px; top: 346px; width: 498px; height: 264px;
    background: linear-gradient(180deg, #efe3d2 0%, #d8b48a 35%, #b98450 70%, #a06b3a 100%);
    border: 1px solid var(--copper-soft);
  }
  .appellation {
    top: 656px; font-family: var(--sans); font-weight: 500;
    font-size: 44px; letter-spacing: 1px; color: var(--ink-dark); line-height: 1;
  }
  .region {
    top: 750px; font-family: var(--sans); font-weight: 400;
    font-size: 22px; letter-spacing: 5px; color: var(--copper); line-height: 1;
  }

  .front-band {
    left: 23px; top: 834px; width: 563px; height: 350px;
    background: var(--band); border-radius: 3px;
    box-shadow: 0 2px 6px rgba(0,0,0,.2);
  }
  .front-band .frame {
    position: absolute; inset: 12px;
    border: 1px solid var(--band-line);
  }
  .vintage {
    top: 108px; font-family: var(--sans); font-weight: 500;
    font-size: 38px; color: var(--copper); line-height: 1;
  }
  .varietal {
    top: 156px; font-family: var(--sans); font-weight: 500;
    font-size: 38px; color: var(--copper); line-height: 1;
  }
  .band-note {
    font-family: var(--sans); font-size: 14px; letter-spacing: 3px;
    color: #c9cdd6; line-height: 1;
  }

  /* Back label */
  .back {
    left: 613px; top: 23px; width: 585px; height: 1155px;
    background: var(--paper);
    border: 1px solid var(--paper-edge);
    border-radius: 20px 20px 4px 4px;
    box-shadow: 0 2px 6px rgba(0,0,0,.12);
  }
  .back-story {
    position: absolute; left: 14px; top: 18px; width: 555px; height: 803px;
    border: 1px solid #b9b2a4; border-radius: 14px 14px 0 0;
  }
  .back-legal {
    position: absolute; left: 14px; top: 830px; width: 555px; height: 310px;
    border: 1px solid #b9b2a4;
  }
  .arch-title { width: 585px; height: 70px; }
  .arch-title text {
    font-family: var(--serif); font-weight: 600; font-size: 25px;
    letter-spacing: 2px; fill: var(--ink-dark);
  }
  .cellar-art {
    left: 172px; top: 140px; width: 218px; height: 118px;
    background: linear-gradient(180deg, #e6d3b8 0%, #c49563 60%, #a87340 100%);
    border-radius: 3px;
  }
  .year-mark {
    top: 213px; font-family: var(--text); font-size: 16px; color: var(--ink-dark);
  }
  .rule { height: 1px; background: var(--rule); left: 73px; width: 422px; }
  .bottler {
    top: 307px; font-family: var(--sans); font-weight: 500;
    font-size: 21px; color: var(--ink-dark); line-height: 30px; letter-spacing: .5px;
  }
  .estate-line {
    top: 401px; font-family: var(--sans); font-size: 14px;
    letter-spacing: 2px; color: var(--copper);
  }
  .estate-name {
    top: 424px; font-family: var(--serif); font-weight: 700;
    font-size: 36px; letter-spacing: 1px; color: var(--ink-navy); line-height: 1;
  }
  .estate-tagline {
    top: 468px; font-family: var(--sans); font-size: 13px;
    letter-spacing: 2px; color: var(--copper);
  }
  .story-text {
    left: 64px; top: 546px; width: 456px;
    font-family: var(--text); font-size: 13.5px; line-height: 20px;
    color: var(--ink-body); text-align: justify;
  }
  .address {
    left: 64px; top: 750px; font-family: var(--text);
    font-size: 13.5px; line-height: 21px; color: var(--ink-body);
  }
  .seal {
    left: 450px; top: 750px; width: 30px; height: 30px;
    border: 1.5px solid var(--copper); border-radius: 50%;
  }

  .warning-head {
    left: 24px; top: 24px; font-family: var(--sans); font-weight: 600;
    font-size: 18px; line-height: 24px; color: var(--ink-dark);
  }
  .warning-text {
    left: 24px; top: 56px; width: 505px;
    font-family: var(--text); font-size: 11.5px; line-height: 16px;
    color: var(--ink-body); text-align: justify;
  }
  .legal-rule { left: 14px; width: 525px; height: 1px; background: var(--rule); }
  .abv {
    left: 24px; top: 172px; font-family: var(--sans); font-weight: 500;
    font-size: 20px; color: var(--ink-dark);
  }
  .abv-divider { left: 238px; top: 174px; width: 1px; height: 24px; background: #555; }
  .volume {
    left: 258px; top: 172px; font-family: var(--sans); font-weight: 500;
    font-size: 20px; color: var(--ink-dark);
  }
  .type-note {
    left: 24px; top: 262px; font-family: var(--text); font-size: 12px;
    line-height: 16px; color: var(--ink-body);
  }
  .foot-divider { left: 100px; top: 246px; width: 1px; height: 63px; background: var(--rule); }
  .sulfites {
    left: 138px; top: 270px; font-family: var(--sans); font-weight: 500;
    font-size: 15px; letter-spacing: .5px; color: var(--ink-dark);
  }
</style>
</head>
<body>
<main class="canvas">

  <section class="abs front-main" aria-label="Front label">
    <div class="frame"></div>
    <h1 class="abs center brand-name">FERRANT</h1>
    <div class="abs center brand-sub">ESTATE</div>
    <div class="abs vineyard-art" role="img" aria-label="Engraved view of vineyard rows on rolling mountain hills"></div>
    <div class="abs center appellation">HOWELL MOUNTAIN</div>
    <div class="abs center region">NAPA VALLEY</div>
  </section>

  <section class="abs front-band" aria-label="Front neck band">
    <div class="frame"></div>
    <div class="abs center vintage">2022</div>
    <div class="abs center varietal">CABERNET SAUVIGNON</div>
    <div class="abs center band-note" style="top:240px;">HOWELL MOUNTAIN</div>
    <div class="abs center band-note" style="top:262px;">ESTATE GROWN VINTAGE</div>
  </section>

  <section class="abs back" aria-label="Back label">
    <div class="back-story">
      <svg class="abs arch-title" viewBox="0 0 585 70" style="left:-14px;top:52px;">
        <path id="arch" d="M150 62 Q292 6 434 62" fill="none"/>
        <text text-anchor="middle"><textPath href="#arch" startOffset="50%">· HOWELL MOUNTAIN</textPath></text>
      </svg>
      <div class="abs cellar-art" role="img" aria-label="Engraving of the estate farmhouse"></div>
      <div class="abs year-mark" style="left:74px;">2022</div>
      <div class="abs year-mark" style="left:440px;">2022</div>

      <div class="abs rule" style="top:288px;"></div>
      <div class="abs center bottler">CELLARED AND BOTTLED BY<br>ANGWIN, CA 94508</div>
      <div class="abs rule" style="top:385px;"></div>

      <div class="abs center estate-line">CELLARED AND ESTATE BOTTLED BY</div>
      <div class="abs center estate-name">FERRANT ESTATE</div>
      <div class="abs center estate-tagline">FAMILY OWNED AND OPERATED</div>
      <div class="abs rule" style="top:508px;"></div>

      <p class="abs story-text">Grown on the volcanic slopes of Howell Mountain, high above the fog line of Napa Valley, our Cabernet Sauvignon ripens slowly in thin red soils and cool mountain air. Each lot is picked by hand, fermented in small batches and aged in French oak before bottling at the estate. Dark fruit, firm structure and a long, quiet finish reward patient cellaring.</p>

      <p class="abs address">Ferrant Estate, Angwin, CA 94508<br>Estate grown and bottled</p>
      <div class="abs seal"></div>
    </div>

    <div class="back-legal">
      <div class="abs warning-head">GOVERNMENT WARNING:</div>
      <p class="abs warning-text">(1) According to the Surgeon General, women should not drink alcoholic beverages during pregnancy because of the risk of birth defects. (2) Consumption of alcoholic beverages impairs your ability to drive a car or operate machinery, and may cause health problems.</p>
      <div class="abs legal-rule" style="top:146px;"></div>
      <div class="abs abv">ALC. 14.5% BY VOL.</div>
      <div class="abs abv-divider"></div>
      <div class="abs volume">750 ML</div>
      <div class="abs legal-rule" style="top:238px;"></div>
      <div class="abs type-note">Red<br>Wine</div>
      <div class="abs foot-divider"></div>
      <div class="abs sulfites">CONTAINS SULFITES</div>
    </div>
  </section>

</main>
</body>
</html>
```